Project Transparent, Clean, and Simple.

Please use the current website for any materials: www.venholdrusk.com - I don't have anything that I can upload - sorry :)

To clarify we want to create pages for each tab on the existing site. If you think there is a better way to group these or showcase these categories please feel free to do so but please include these pages.

1.Home Page
Your Needs should each have a separate page
2. Family Office
3. Entrepreneurs
4.Clear Duty
5. Your Team
6. Insights
7. News & Media
8. Contact Us

We just want this site to look like Quiller.com. Simple. Easy. Impactful.
Current website again is:
https://www.venholdrusk.com/

We are doing something completely different from everyone else in our industry, and we want people to realize that this is not an ordinary place. We want to bring transparency to our clients, make them feel comfortable and gain trust in our beliefs. We provide everything from doing your taxes, travel planning, financial planning, estate planning, legal work, family and life management issues - etc. Our main service is managing money but with the obligation of providing our clients options that have their best interests in mind - which most banks cannot and do not do.

If our site does not show that we are simple, transparent, and easy to use. We won't be able to get that far. It also needs to be easy enough to view videos and for people to sign up to learn more without being in front of your face as the main call to action.

Target Market(s)

Entrepreneurs and High Net Worth Individuals

Industry/Entity Type

Financial Service

Number of Pages Required

5+ page

Font styles to use
Sans Serif
Other font styles liked:
• Times New Roman, Palatino, Georgia, Courier, Bookman and Garamond

Colors
1b1b1b
ffffff
0292cd

Requirements
Must have
• Simple. A lot of White Space. Needs to look as simple and impactful as Quiller.com.
Nice to have
• White Space
Should not have
• A lot of colors. Not much White Space. Busy.

```html
<!DOCTYPE html>
<html lang="en">
<head>
<meta charset="utf-8">
<title>VenholdRusk — Transparent Family Wealth Advisors</title>
<link rel="stylesheet" href="https://fonts.googleapis.com/css2?family=Cinzel:wght@400;700&family=Open+Sans:wght@400;600;700&family=Tinos:wght@400;700&display=swap">
<style>
:root{
  --ink:#1b1b1b;
  --white:#ffffff;
  --blue:#0292cd;
  --blue-deep:#0a6fa6;
  --text:#555a60;
  --muted:#8a8f95;
  --rule:#d9dcdf;
  --card:#efefef;
  --footer:#2b2d31;
  --footer-side:#1f2023;
  --footer-text:#b9bcc1;
}
*{box-sizing:border-box;margin:0;padding:0}
html,body{width:1200px;height:4523px;overflow:hidden}
body{position:relative;background:var(--white);font-family:"Open Sans",Arial,sans-serif;color:var(--text)}

/* header */
.topbar{position:absolute;left:0;top:0;width:1200px;height:78px;background:var(--ink)}
.brand{position:absolute;left:54px;top:12px;display:flex;align-items:center;gap:10px;color:var(--white)}
.brand-mark{width:22px;height:22px;background:var(--white)}
.brand-name{font-size:28px;font-weight:700;line-height:1}
.brand-tag{position:absolute;left:54px;top:46px;font-size:11px;color:#cfd2d6}
.info{position:absolute;top:14px;display:flex;gap:10px;color:var(--white);font-size:13px;line-height:1.35}
.info strong{display:block;font-size:14px}
.info svg{flex:none}

.nav{position:absolute;left:48px;top:78px;width:1104px;height:42px;background:var(--blue);display:flex;align-items:center;padding-left:22px;z-index:2}
.nav a{color:var(--white);text-decoration:none;font-size:13px;font-weight:600;text-transform:uppercase;padding:0 25px}
.nav a:first-child{padding-left:0}

.hero{position:absolute;left:0;top:120px;width:1200px;height:558px;background:linear-gradient(120deg,#dfe4ea 0%,#9aa3ad 40%,#3a3f47 70%,#cbd2d9 100%)}
.about-box{position:absolute;left:48px;top:618px;width:1104px;height:272px;background:var(--blue);color:var(--white);text-align:center;padding:26px 40px 0}
.about-box h2{font-family:"Cinzel",Georgia,serif;font-size:38px;font-weight:700;letter-spacing:1px}
.about-box p{font-size:14px;line-height:1.65;margin-top:14px}
.btn-outline{display:inline-block;margin-top:20px;border:2px solid var(--white);padding:8px 30px;font-family:"Cinzel",Georgia,serif;font-weight:700;font-size:14px;letter-spacing:1px}

/* services */
.services{position:absolute;left:0;top:965px;width:1200px;display:flex;justify-content:space-between;padding:0 48px}
.service{width:340px;text-align:center}
.service-icon{width:124px;height:124px;border-radius:50%;background:var(--ink);margin:0 auto;display:flex;align-items:center;justify-content:center}
.service h3{font-size:20px;font-weight:600;color:#333;margin-top:20px}
.service p{font-size:14px;line-height:1.6;color:var(--muted);margin-top:12px}

/* numbers */
.numbers{position:absolute;left:0;top:1290px;width:1200px;height:227px;background:var(--ink);color:var(--white)}
.numbers h2{font-family:"Cinzel",Georgia,serif;font-size:36px;text-align:center;margin-top:18px;font-weight:400;letter-spacing:1px}
.stat{position:absolute;top:92px;width:200px;margin-left:-100px;text-align:center}
.stat b{display:block;font-size:46px;font-weight:700;line-height:1}
.stat i{display:block;width:60px;height:3px;background:var(--white);margin:10px auto 12px}
.stat span{font-size:13px;color:#c8cbcf}

/* timeline */
.section-title{position:absolute;left:0;width:1200px;text-align:center;font-family:"Cinzel",Georgia,serif;font-size:40px;color:#333;letter-spacing:1px}
.spine{position:absolute;left:596px;top:1660px;width:8px;height:560px;background:#bfc3c7;border-radius:4px}
.tl-item{position:absolute;width:430px}
.tl-item h4{font-size:20px;font-weight:600;color:#333}
.tl-item p{font-size:12px;line-height:1.5;color:var(--muted);margin-top:4px}
.tl-left{left:113px;text-align:right}
.tl-right{left:657px}
.tl-dot{position:absolute;left:584px;width:32px;height:32px;border-radius:50%;background:var(--blue);border:3px solid var(--white);box-shadow:0 0 0 1px var(--rule);display:flex;align-items:center;justify-content:center}
.tl-dot i{width:10px;height:10px;background:var(--white)}

/* sudden wealth */
.wealth{position:absolute;left:0;top:2276px;width:1200px;height:564px;background:linear-gradient(100deg,#0a79b8 0%,#0292cd 45%,#5fb6de 100%)}
.wealth-photo{position:absolute;left:588px;top:0;width:612px;height:564px;background:linear-gradient(90deg,rgba(160,200,225,.4),#8fb3c9 40%,#5b6f7f 100%)}
.wealth h2{position:absolute;left:0;top:20px;width:1200px;text-align:center;font-family:"Cinzel",Georgia,serif;font-size:40px;color:var(--white);font-weight:400;letter-spacing:1px}
.wealth-copy{position:absolute;left:54px;top:98px;width:540px;color:var(--white);font-family:"Tinos","Times New Roman",serif;font-size:15px;line-height:1.4;font-weight:700}
.wealth-copy h3{font-size:21px;margin-top:16px}
.badge{position:absolute;width:160px;margin-left:-80px;text-align:center;color:var(--white);font-family:"Tinos","Times New Roman",serif;font-weight:700;font-size:14px}
.badge-icon{width:104px;height:104px;border-radius:50%;background:var(--ink);margin:0 auto 8px;display:flex;align-items:center;justify-content:center;border:3px solid rgba(255,255,255,.25)}

/* team */
.team{position:absolute;left:54px;top:2985px;width:1092px;display:flex;justify-content:space-between}
.member{width:247px;height:416px;background:var(--card);border:1px solid #e2e2e2;padding:9px 9px 0;text-align:center;overflow:hidden}
.member-photo{height:157px;background:linear-gradient(160deg,#c9b9a8,#6d5f54 60%,#3a3330)}
.member h4{font-family:"Cinzel",Georgia,serif;font-size:18px;font-weight:700;color:#333;margin-top:18px;letter-spacing:1px}
.member p{font-family:"Tinos","Times New Roman",serif;font-size:14px;line-height:21px;max-height:147px;overflow:hidden;color:#666;margin-top:10px;padding:0 6px}

/* call back */
.callback{position:absolute;left:0;top:3558px;width:1200px;height:407px;background:linear-gradient(90deg,#ffffff 0%,#f3f4f6 60%,#e9ebee 100%)}
.callback-photo{position:absolute;left:0;top:0;width:452px;height:407px;background:linear-gradient(180deg,#f1f2f4,#c9d7e6 60%,#8fb2d3)}
.callback-kicker{position:absolute;left:458px;top:54px;font-family:"Cinzel",Georgia,serif;font-size:22px;color:#333;letter-spacing:1px}
.callback-title{position:absolute;left:458px;top:84px;font-family:"Cinzel",Georgia,serif;font-size:40px;font-weight:700;color:var(--blue);letter-spacing:1px}
.callback-text{position:absolute;left:458px;top:140px;width:600px;font-size:12px;line-height:1.6;color:#666}
.field{position:absolute;height:42px;background:var(--white);border:1px solid var(--rule);font-size:12px;color:#888;padding:0 14px;display:flex;align-items:center}
.field-select{justify-content:space-between}
.btn-wait{position:absolute;left:995px;top:331px;width:160px;height:42px;border:2px solid var(--blue);color:var(--blue);font-size:13px;font-weight:700;display:flex;align-items:center;justify-content:center;background:var(--white)}

/* footer */
.footer{position:absolute;left:0;top:3965px;width:1200px;height:467px;background:var(--footer);color:var(--footer-text)}
.footer-side{position:absolute;left:0;top:0;width:362px;height:467px;background:var(--footer-side)}
.footer-map{position:absolute;left:115px;top:75px;width:223px;height:121px;background:linear-gradient(135deg,#e8e6df,#cfd8c4 55%,#b9cde0)}
.footer-side h5{position:absolute;left:115px;top:222px;font-size:16px;color:var(--white);font-weight:700}
.contact-line{position:absolute;left:115px;display:flex;gap:12px;font-size:12px;line-height:1.5;color:var(--footer-text);width:230px}
.footer-col{position:absolute;top:75px;width:232px}
.footer-col h5{font-size:16px;color:var(--white);font-weight:700;text-transform:uppercase;padding-bottom:14px;border-bottom:1px solid #45484e}
.links li{list-style:none;font-size:12px;color:var(--white);padding:16px 0 16px 16px;border-bottom:1px solid #3d4045;position:relative}
.links li::before{content:"";position:absolute;left:0;top:21px;border-left:5px solid var(--white);border-top:4px solid transparent;border-bottom:4px solid transparent}
.news{display:flex;gap:12px;padding:16px 0;border-bottom:1px solid #3d4045}
.news-date{width:40px;height:40px;background:var(--white);color:var(--ink);text-align:center;font-size:15px;font-weight:700;line-height:1.1;padding-top:4px;flex:none}
.news-date small{display:block;font-size:9px;font-weight:400}
.news p{font-size:12px;line-height:1.4;color:var(--white)}
.news span{display:block;font-size:11px;color:var(--footer-text);margin-top:4px}
.gallery{display:grid;grid-template-columns:repeat(3,74px);gap:8px;margin-top:24px}
.gallery div{height:74px;background:linear-gradient(135deg,#dfe6ee,#98a7b8)}
.bottombar{position:absolute;left:0;top:4432px;width:1200px;height:91px;background:var(--blue);color:var(--white)}
.bottombar p{position:absolute;left:115px;top:36px;font-size:13px}
.socials{position:absolute;left:995px;top:34px;display:flex;gap:8px}
.socials span{width:24px;height:24px;border:1px solid rgba(255,255,255,.8);border-radius:2px}
</style>
</head>
<body>

<header class="topbar">
  <div class="brand"><span class="brand-mark"></span><span class="brand-name">VenholdRusk</span></div>
  <div class="brand-tag">Transparent Family Wealth Advisors</div>
  <div class="info" style="left:660px">
    <svg width="22" height="28" viewBox="0 0 22 28"><path d="M11 1a9 9 0 0 0-9 9c0 7 9 17 9 17s9-10 9-17a9 9 0 0 0-9-9z" fill="#fff"/><circle cx="11" cy="10" r="3.5" fill="#1b1b1b"/></svg>
    <div><strong>Address</strong>18 - elm row London U.K</div>
  </div>
  <div class="info" style="left:940px">
    <svg width="28" height="28" viewBox="0 0 28 28"><circle cx="14" cy="14" r="12" fill="none" stroke="#fff" stroke-width="2.5"/><path d="M14 7v7l5 3" stroke="#fff" stroke-width="2.5" fill="none"/></svg>
    <div><strong>Open Hours</strong>11 : 00 A.M - 08 : 00 P.M</div>
  </div>
</header>

<nav class="nav">
  <a href="#">Home</a><a href="#">Your Needs</a><a href="#">Your Team</a><a href="#">Insights</a><a href="#">News and Media</a><a href="#">Contact Us</a>
</nav>

<div class="hero" role="img" aria-label="Photo of smiling advisors in business suits in an office"></div>

<section class="about-box">
  <h2>WHO WE ARE</h2>
  <p>Consistently ranked as a national top advisor by Ledgerline, Marketwise and Capital Courier, VenholdRusk is one of America’s premier independent family wealth advisors. As a family office for ultra-high-net-worth individuals, entrepreneurs going through a liquidity event and their families, our customer focused philosophy is rooted in the Clear Duty principles we created. VenholdRusk represents $2.5 billion in assets under advisement and we are frequent expert contributors to national media seeking input on global market activity and financial industry governance.</p>
  <span class="btn-outline">READ MORE</span>
</section>

<section class="services">
  <div class="service">
    <div class="service-icon"><svg width="70" height="70" viewBox="0 0 70 70"><circle cx="35" cy="35" r="28" fill="none" stroke="#fff" stroke-width="3"/><text x="35" y="46" text-anchor="middle" font-family="Open Sans,sans-serif" font-size="32" font-weight="700" fill="#fff">$</text></svg></div>
    <h3>Investment Management</h3>
    <p>Fee-based, unbiased advisory services to give you peace of mind what you’ve earned will be protected.</p>
  </div>
  <div class="service">
    <div class="service-icon"><svg width="70" height="70" viewBox="0 0 70 70"><circle cx="14" cy="18" r="5" fill="#fff"/><path d="M8 60V34a6 6 0 0 1 12 0v26" fill="#fff"/><path d="M28 18l8 8M36 18l-8 8M54 40a5 5 0 1 1-.1 0M30 52c10-2 16-10 18-22" stroke="#fff" stroke-width="3" fill="none"/><path d="M44 28l6 0 0 6" stroke="#fff" stroke-width="3" fill="none"/></svg></div>
    <h3>Wealth Planning and Coordination</h3>
    <p>Highly personal strategy and tactics to address things like tax minimization and cash-flow to fuel your lifestyle.</p>
  </div>
  <div class="service">
    <div class="service-icon"><svg width="70" height="70" viewBox="0 0 70 70"><g fill="#fff"><circle cx="15" cy="16" r="6"/><rect x="9" y="24" width="12" height="30" rx="3"/><circle cx="35" cy="14" r="6"/><rect x="29" y="22" width="12" height="32" rx="3"/><circle cx="55" cy="16" r="6"/><rect x="49" y="24" width="12" height="30" rx="3"/></g></svg></div>
    <h3>Family Leadership</h3>
    <p>Fee-based, unbiased advisory services to give you peace of mind what you’ve earned will be protected.</p>
  </div>
</section>

<section class="numbers">
  <h2>OUR NUMBERS</h2>
  <div class="stat" style="left:211px"><b>405+</b><i></i><span>Customers</span></div>
  <div class="stat" style="left:470px"><b>78+</b><i></i><span>Awards</span></div>
  <div class="stat" style="left:748px"><b>1,510+</b><i></i><span>Projects</span></div>
  <div class="stat" style="left:1019px"><b>55+</b><i></i><span>Members</span></div>
</section>

<h2 class="section-title" style="top:1556px">WHO WE ARE</h2>
<div class="spine"></div>

<div class="tl-item tl-left" style="top:1690px"><h4>Investment Strategy and Execution</h4><p>Venhold Rusk is uniquely focused on providing 360° financial advisory and family support to the American entrepreneur both.</p></div>
<div class="tl-item tl-left" style="top:1793px"><h4>Banking Services</h4><p>Venhold Rusk is uniquely focused on providing 360° financial advisory and family support to the American entrepreneur both.</p></div>
<div class="tl-item tl-left" style="top:1895px"><h4>Cashflow Management</h4><p>Venhold Rusk is uniquely focused on providing 360° financial advisory and family support to the American entrepreneur both.</p></div>
<div class="tl-item tl-left" style="top:1998px"><h4>Credit Planning</h4><p>Venhold Rusk is uniquely focused on providing 360° financial advisory and family support to the American entrepreneur both.</p></div>
<div class="tl-item tl-left" style="top:2100px"><h4>Tax Minimization</h4><p>Venhold Rusk is uniquely focused on providing 360° financial advisory and family support to the American entrepreneur both.</p></div>

<div class="tl-item tl-right" style="top:1690px"><h4>Travel and Entertainment</h4><p>Venhold Rusk is uniquely focused on providing 360° financial advisory and family support to the American entrepreneur both.</p></div>
<div class="tl-item tl-right" style="top:1793px"><h4>Family and Life Management Issues</h4><p>Venhold Rusk is uniquely focused on providing 360° financial advisory and family support to the American entrepreneur both.</p></div>
<div class="tl-item tl-right" style="top:1895px"><h4>Access to Legal Advisory</h4><p>Venhold Rusk is uniquely focused on providing 360° financial advisory and family support to the American entrepreneur both.</p></div>
<div class="tl-item tl-right" style="top:1998px"><h4>Estate Planning</h4><p>Venhold Rusk is uniquely focused on providing 360° financial advisory and family support to the American entrepreneur both.</p></div>
<div class="tl-item tl-right" style="top:2100px"><h4>Philanthropy</h4><p>Venhold Rusk is uniquely focused on providing 360° financial advisory and family support to the American entrepreneur both.</p></div>

<div class="tl-dot" style="top:1712px"><i></i></div>
<div class="tl-dot" style="top:1815px"><i></i></div>
<div class="tl-dot" style="top:1917px"><i></i></div>
<div class="tl-dot" style="top:2020px"><i></i></div>
<div class="tl-dot" style="top:2122px"><i></i></div>

<section class="wealth">
  <div class="wealth-photo" role="img" aria-label="Photo of two businessmen shaking hands"></div>
  <h2>WHO WE ARE</h2>
  <div class="wealth-copy">
    <p>Venhold Rusk is uniquely focused on providing 360° financial advisory and family support to the American entrepreneur both before and after a liquidity event.</p>
    <h3>We also support sudden-wealth situations such as:</h3>
  </div>
  <div class="badge" style="left:130px;top:240px"><div class="badge-icon"><svg width="50" height="56" viewBox="0 0 50 56"><path d="M15 2h20l-6 16h-8z" fill="#fff"/><circle cx="25" cy="36" r="16" fill="none" stroke="#fff" stroke-width="3"/><path d="M25 27l3 6 6 1-4 4 1 6-6-3-6 3 1-6-4-4 6-1z" fill="#fff"/></svg></div>INHERITANCE</div>
  <div class="badge" style="left:416px;top:240px"><div class="badge-icon"><svg width="60" height="40" viewBox="0 0 60 40"><rect x="3" y="6" width="54" height="28" rx="3" fill="none" stroke="#fff" stroke-width="3"/><circle cx="30" cy="20" r="7" fill="none" stroke="#fff" stroke-width="3"/><circle cx="13" cy="20" r="2.5" fill="#fff"/><circle cx="47" cy="20" r="2.5" fill="#fff"/></svg></div>LOTTERY</div>
  <div class="badge" style="left:130px;top:400px"><div class="badge-icon"><svg width="54" height="50" viewBox="0 0 54 50"><path d="M27 46S4 31 4 16A11 11 0 0 1 27 10a11 11 0 0 1 23 6c0 15-23 30-23 30z" fill="none" stroke="#fff" stroke-width="3"/><path d="M27 12l-5 12 8 6-5 14" fill="none" stroke="#fff" stroke-width="3"/></svg></div>DIVORCE</div>
  <div class="badge" style="left:416px;top:400px"><div class="badge-icon"><svg width="56" height="50" viewBox="0 0 56 50"><path d="M6 36L3 12l14 10 11-16 11 16 14-10-3 24z" fill="none" stroke="#fff" stroke-width="3"/><rect x="7" y="40" width="42" height="5" fill="#fff"/></svg></div>PRO ATHLETES</div>
</section>

<h2 class="section-title" style="top:2888px">FEATURED TEAM MEMBERS</h2>
<section class="team">
  <article class="member"><div class="member-photo" role="img" aria-label="Portrait photo of team member Clara Wendt"></div><h4>CLARA WENDT</h4><p>As the Director of Financial Planning, Clara works in concert with Venhold Rusk’s Premier Family Office to identify and analyze the challenges facing their high-net-worth clients, and then develops sophisticated and custom financial plans and strategies to</p></article>
  <article class="member"><div class="member-photo" role="img" aria-label="Portrait photo of team member Morris Hale"></div><h4>MORRIS HALE</h4><p>As the Director of Financial Planning, Morris works in concert with Venhold Rusk’s Premier Family Office to identify and analyze the challenges facing their high-net-worth clients, and then develops sophisticated and custom financial plans and strategies to</p></article>
  <article class="member"><div class="member-photo" role="img" aria-label="Portrait photo of team member Irena Basko"></div><h4>IRENA BASKO</h4><p>As the Director of Financial Planning, Irena works in concert with Venhold Rusk’s Premier Family Office to identify and analyze the challenges facing their high-net-worth clients, and then develops sophisticated and custom financial plans and strategies to</p></article>
  <article class="member"><div class="member-photo" role="img" aria-label="Portrait photo of team member Daniel Royce"></div><h4>DANIEL ROYCE</h4><p>As the Director of Financial Planning, Daniel works in concert with Venhold Rusk’s Premier Family Office to identify and analyze the challenges facing their high-net-worth clients, and then develops sophisticated and custom financial plans and strategies to</p></article>
</section>

<section class="callback">
  <div class="callback-photo" role="img" aria-label="Photo of a smiling woman in glasses holding a phone"></div>
  <div class="callback-kicker">WE ARE ALWAYS READY</div>
  <div class="callback-title">REQUEST A CALL BACK</div>
  <p class="callback-text">Consectetur adipisicing elit sed do eiusmod tempor incididunt ut labore et dolore lqua Ut enim ad minim veniam, quis nostrud exercitation ullamco Consectetur adipisicing elit sed do eiusmod tempor incididunt.</p>
  <div class="field" style="left:458px;top:271px;width:220px">Your Name</div>
  <div class="field" style="left:696px;top:271px;width:220px">Your Number</div>
  <div class="field" style="left:935px;top:271px;width:220px">Your Email</div>
  <div class="field field-select" style="left:458px;top:331px;width:507px">I Would Like To Discuss<svg width="10" height="6" viewBox="0 0 10 6"><path d="M0 0h10L5 6z" fill="#888"/></svg></div>
  <div class="btn-wait">I'M WAITING</div>
</section>

<footer class="footer">
  <div class="footer-side">
    <div class="footer-map" role="img" aria-label="Map showing the head office location"></div>
    <h5>HEAD OFFICE</h5>
    <div class="contact-line" style="top:252px"><svg width="12" height="16" viewBox="0 0 12 16"><path d="M6 0a6 6 0 0 0-6 6c0 4 6 10 6 10s6-6 6-10a6 6 0 0 0-6-6z" fill="#b9bcc1"/></svg><span>47 Harrow Mill Lane, Southgate Road, East London, UK, N4 2QT</span></div>
    <div class="contact-line" style="top:310px"><svg width="14" height="12" viewBox="0 0 14 12"><rect x="1" y="1" width="12" height="10" fill="none" stroke="#b9bcc1" stroke-width="1.5"/><path d="M1 1l6 5 6-5" fill="none" stroke="#b9bcc1" stroke-width="1.5"/></svg><span>hello@venholdrusk.com</span></div>
    <div class="contact-line" style="top:346px"><svg width="14" height="14" viewBox="0 0 14 14"><path d="M3 1l3 3-2 2a8 8 0 0 0 4 4l2-2 3 3-2 2C6 13 1 8 1 3z" fill="#b9bcc1"/></svg><span>+44 100 200 300 - 0</span></div>
  </div>
  <div class="footer-col" style="left:377px">
    <h5>Useful Links</h5>
    <ul class="links"><li>Wealth Planning</li><li>Investment Management</li><li>Year-End Tax Planning</li><li>Tax Advisory Services</li><li>Small Business Taxes</li></ul>
  </div>
  <div class="footer-col" style="left:639px">
    <h5>Recent News</h5>
    <div class="news"><div class="news-date">04<small>Dec</small></div><p>Claritas dynamicus qui sequunt mutationem consuetu.<span>24 Min Ago</span></p></div>
    <div class="news"><div class="news-date">04<small>Dec</small></div><p>Claritas dynamicus qui sequunt mutationem consuetu.<span>24 Min Ago</span></p></div>
    <div class="news"><div class="news-date">04<small>Dec</small></div><p>Claritas dynamicus qui sequunt mutationem consuetu.<span>24 Min Ago</span></p></div>
  </div>
  <div class="footer-col" style="left:901px">
    <h5>Photo Widget</h5>
    <div class="gallery">
      <div role="img" aria-label="Photo of a model house and coins"></div>
      <div role="img" aria-label="Photo of an advisor at work"></div>
      <div role="img" aria-label="Photo of a client meeting"></div>
      <div role="img" aria-label="Photo of a family"></div>
      <div role="img" aria-label="Photo of a business team"></div>
      <div role="img" aria-label="Photo of an office"></div>
    </div>
  </div>
</footer>

<div class="bottombar">
  <p>© 2016 | All Rights Reserved</p>
  <div class="socials"><span></span><span></span><span></span><span></span><span></span></div>
</div>

</body>
</html>
```